regPersonal Trainer Flyer Design

Reason: I have been very busy with other work and would like to extend the deadline to offer designers the chance to edit and improve designs with my help. Thank you for all the designs that have been sent so far.

```html
<!DOCTYPE html>
<html lang="en">
<head>
<meta charset="utf-8">
<title>Personal Trainer Flyer</title>
<link href="https://fonts.googleapis.com/css2?family=Fira+Sans:ital,wght@0,300;0,400;0,600;0,700;1,900&display=swap" rel="stylesheet">
<style>
  :root {
    --page: #e4e4e4;
    --blue: #0b5cc6;
    --blue-deep: #083f9c;
    --blue-light: #2f78d8;
    --orange: #f39200;
    --orange-light: #ffc21a;
    --yellow: #ffd200;
    --band-dark: #211e1f;
    --grey-photo: #7d7d7d;
    --grey-photo-dark: #4e4e4e;
    --white: #ffffff;
    --ink: #1b1b1b;
  }
  * { margin: 0; padding: 0; box-sizing: border-box; }
  html, body {
    width: 1200px;
    height: 1024px;
    overflow: hidden;
    background: var(--page);
    font-family: "Fira Sans", Arial, sans-serif;
  }
  .flyer {
    position: absolute;
    left: 40px;
    top: 132px;
    width: 1120px;
    height: 760px;
    overflow: hidden;
    box-shadow: 0 10px 28px rgba(0,0,0,0.25);
  }
  .flyer-art {
    position: absolute;
    inset: 0;
    width: 1120px;
    height: 760px;
  }
  .offer {
    position: absolute;
    left: 214px;
    top: 250px;
    transform: rotate(-58deg);
    transform-origin: left top;
    color: var(--white);
    font-size: 26px;
    font-weight: 300;
    line-height: 30px;
    white-space: nowrap;
  }
  .offer strong { font-weight: 700; }
  .pain-points {
    position: absolute;
    left: 690px;
    top: 28px;
    list-style: none;
    color: var(--white);
    font-size: 19px;
    font-weight: 600;
    line-height: 26px;
  }
  .pain-points li {
    position: relative;
    padding-left: 26px;
  }
  .pain-points li::before {
    content: "";
    position: absolute;
    left: 0;
    top: 7px;
    width: 12px;
    height: 12px;
    border-radius: 50%;
    background: var(--yellow);
  }
  .headline {
    position: absolute;
    left: 232px;
    top: 292px;
    width: 440px;
    line-height: 1;
  }
  .headline-main {
    display: block;
    font-size: 100px;
    font-weight: 900;
    font-style: italic;
    color: var(--blue);
    letter-spacing: 3px;
    -webkit-text-stroke: 6px var(--white);
    paint-order: stroke fill;
    text-shadow: 3px 4px 2px rgba(0,0,0,0.35);
  }
  .headline-sub {
    display: block;
    margin-top: 4px;
    text-align: right;
    font-size: 68px;
    font-weight: 300;
    color: var(--white);
    letter-spacing: 1px;
    text-shadow: 1px 2px 3px rgba(0,0,0,0.4);
  }
  .trainer {
    position: absolute;
    left: 712px;
    top: 494px;
    transform: rotate(-2.9deg);
    transform-origin: left top;
  }
  .trainer-name {
    color: var(--yellow);
    font-size: 46px;
    font-weight: 400;
    line-height: 62px;
    white-space: nowrap;
  }
  .trainer-role {
    margin-top: 6px;
    color: var(--ink);
    font-size: 28px;
    font-weight: 400;
    line-height: 38px;
    white-space: nowrap;
  }
  .contact {
    position: absolute;
    left: 712px;
    top: 624px;
    color: var(--white);
    transform: rotate(-2.9deg);
    transform-origin: left top;
    white-space: nowrap;
  }
  .contact-phone {
    font-size: 38px;
    font-weight: 700;
    line-height: 44px;
    letter-spacing: 0.5px;
  }
  .contact-email {
    font-size: 27px;
    font-weight: 400;
    line-height: 34px;
  }
</style>
</head>
<body>
  <main class="flyer">
    <svg class="flyer-art" viewBox="0 0 1120 760" xmlns="http://www.w3.org/2000/svg">
      <defs>
        <linearGradient id="bg-blue" x1="0" y1="0" x2="0" y2="1">
          <stop offset="0" stop-color="#2f78d8"/>
          <stop offset="0.55" stop-color="#0b5cc6"/>
          <stop offset="1" stop-color="#083f9c"/>
        </linearGradient>
        <linearGradient id="orange-fade" x1="0" y1="0" x2="1" y2="0">
          <stop offset="0" stop-color="#ffc21a"/>
          <stop offset="1" stop-color="#f39200"/>
        </linearGradient>
        <linearGradient id="gym-wall" x1="0" y1="0" x2="0" y2="1">
          <stop offset="0" stop-color="#4e4e4e"/>
          <stop offset="0.5" stop-color="#7d7d7d"/>
          <stop offset="1" stop-color="#4e4e4e"/>
        </linearGradient>
        <radialGradient id="trainer-backdrop" cx="0.5" cy="0.45" r="0.6">
          <stop offset="0" stop-color="#5a7fb3"/>
          <stop offset="0.7" stop-color="#2c64b8"/>
          <stop offset="1" stop-color="#0b5cc6" stop-opacity="0"/>
        </radialGradient>
        <linearGradient id="thumb" x1="0" y1="0" x2="0" y2="1">
          <stop offset="0" stop-color="#b9b2ab"/>
          <stop offset="1" stop-color="#5f5955"/>
        </linearGradient>
        <filter id="soft-shadow" x="-20%" y="-20%" width="140%" height="140%">
          <feDropShadow dx="2" dy="4" stdDeviation="4" flood-opacity="0.35"/>
        </filter>
      </defs>

      <rect class="background" width="1120" height="760" fill="url(#bg-blue)"/>

      <polygon class="accent-orange" points="0,0 330,0 250,760 0,760" fill="url(#orange-fade)"/>

      <polygon class="photo-client" role="img" aria-label="Photo of a woman training with suspension straps against a grey gym wall"
               points="210,0 760,0 700,600 190,600" fill="url(#gym-wall)"/>

      <polygon class="accent-stripe" points="184,232 200,242 298,86 282,76" fill="var(--white)"/>

      <rect class="photo-trainer" role="img" aria-label="Photo of the personal trainer pulling suspension straps"
            x="560" y="170" width="460" height="360" fill="url(#trainer-backdrop)"/>

      <polygon class="band-line" points="140,512 1120,462 1120,470 140,520" fill="var(--white)"/>
      <polygon class="band-dark" points="140,520 1120,470 1120,540 140,590" fill="var(--band-dark)"/>
      <polygon class="band-yellow" points="0,597 1120,540 1120,592 0,649" fill="url(#orange-fade)"/>

      <g class="thumbnails" filter="url(#soft-shadow)">
        <circle cx="250" cy="672" r="56" fill="url(#thumb)" stroke="var(--white)" stroke-width="7" role="img" aria-label="Photo of a boxing pad session"/>
        <circle cx="374" cy="664" r="56" fill="url(#thumb)" stroke="var(--white)" stroke-width="7" role="img" aria-label="Photo of a barbell curl"/>
        <circle cx="498" cy="656" r="56" fill="url(#thumb)" stroke="var(--white)" stroke-width="7" role="img" aria-label="Photo of a dumbbell workout"/>
        <circle cx="622" cy="648" r="56" fill="url(#thumb)" stroke="var(--white)" stroke-width="7" role="img" aria-label="Photo of a pad training session in the gym"/>
      </g>
    </svg>

    <p class="offer">One Month<br><strong>Free</strong> Session</p>

    <ul class="pain-points">
      <li>Lacking motivation?</li>
      <li>Not achieving your goals?</li>
      <li>Need help?</li>
      <li>Bored of the gym?</li>
      <li>You're never too old</li>
      <li>I can help improve your<br>health and well-being</li>
    </ul>

    <h1 class="headline">
      <span class="headline-main">FITNESS</span>
      <span class="headline-sub">TRAINING</span>
    </h1>

    <div class="trainer">
      <p class="trainer-name">Dana Whitlow</p>
      <p class="trainer-role">Personal Trainer</p>
    </div>

    <div class="contact">
      <p class="contact-phone">07700900412</p>
      <p class="contact-email">dana.whitlow@fitmail.co.uk</p>
    </div>
  </main>
</body>
</html>
```